Vehicle Signage

Please design a graphic layout for a Van signage to advertise the business

"Kestrel Vantage Systems"
the logo is in the attached files

Also attached are some icons that represent the fields of service, I would like to use these in the design please
Updates

Reason: I am making some changes to the KVS logo to help match the Vans, I will up load the new files as soon as possible

Target Market(s)

We are targeting people who feel they would like to have some security equipment installed for piece of mind in the the fields of:
"Alarms, Intercoms, CCTV, Access Control"

Industry/Entity Type

Business

Requirements
Must have
• Must be Clear what we do,
it can be icons/pictures or words to represent the service areas of:

```html
<!DOCTYPE html>
<html lang="en">
<head>
<meta charset="utf-8">
<title>Kestrel Vantage Systems – Van Signage</title>
<link rel="stylesheet" href="https://fonts.googleapis.com/css2?family=Oswald:wght@500;600&family=Roboto+Condensed:wght@700&display=swap">
<style>
  :root {
    --canvas: #ffffff;
    --panel: #0d0d0f;
    --panel-edge: #2a2a2e;
    --white: #ffffff;
    --accent: #2aa6e0;
    --brand-blue: #1e8fd6;
    --pill-top: #2f9be0;
    --pill-bottom: #0f5fae;
    --pill-border: #0b2f5c;
    --ink-blue: #1a5db0;
    --figure-dark: #3a3a3e;
    --figure-light: #8a8a90;
  }
  * { margin: 0; padding: 0; box-sizing: border-box; }
  html, body { width: 1200px; height: 565px; overflow: hidden; background: var(--canvas); }
  .signage { position: relative; width: 1200px; height: 565px; }

  .hero-panel { position: absolute; left: 168px; top: 94px; width: 500px; height: 152px; }
  .hero-panel svg { position: absolute; inset: 0; }

  .mascot {
    position: absolute; left: 106px; top: 108px; width: 72px; height: 132px;
    border-radius: 36px 30px 20px 24px;
    background: radial-gradient(circle at 45% 30%, var(--figure-light), var(--figure-dark) 70%);
  }

  .headline {
    position: absolute; left: 194px; top: 114px;
    font-family: 'Oswald', sans-serif; font-weight: 500;
    font-size: 31px; line-height: 34px; color: var(--white);
  }
  .headline .hl { color: var(--accent); }

  .brand-name {
    position: absolute; left: 370px; top: 100px; width: 256px; text-align: center;
    font-family: 'Oswald', sans-serif; font-weight: 600;
    font-size: 92px; line-height: 110px; letter-spacing: 6px; color: var(--brand-blue);
  }
  .brand-tagline {
    position: absolute; left: 370px; top: 204px; width: 256px; text-align: center;
    font-family: 'Roboto Condensed', sans-serif; font-weight: 700;
    font-size: 15px; letter-spacing: 0.3px; color: var(--white);
  }

  .services { position: absolute; left: 184px; top: 257px; display: flex; gap: 7px; list-style: none; }
  .service {
    display: flex; align-items: center; gap: 4px;
    height: 44px; padding: 0 6px 0 4px;
    border: 3px solid var(--pill-border); border-radius: 10px;
    background: linear-gradient(var(--pill-top), var(--pill-bottom));
    font-family: 'Roboto Condensed', sans-serif; font-weight: 700;
    color: var(--white); font-size: 14px; white-space: nowrap; overflow: hidden;
  }
  .service svg { width: 28px; height: 28px; flex: none; }
  .service span { flex: 1; text-align: center; }
  .service.alarms { width: 112px; }
  .service.intercoms { width: 112px; }
  .service.intercoms span { font-size: 13px; letter-spacing: -0.2px; }
  .service.cctv { width: 110px; }
  .service.access { width: 110px; }
  .service.access span { font-size: 12px; line-height: 13px; }

  .phone {
    position: absolute; left: 734px; top: 273px; display: flex; align-items: center; gap: 6px;
    font-family: 'Roboto Condensed', sans-serif; font-weight: 700;
    font-size: 33px; color: var(--ink-blue);
  }
  .phone svg { width: 34px; height: 30px; }

  .website {
    position: absolute; left: 320px; top: 348px;
    font-family: 'Roboto Condensed', sans-serif; font-weight: 700;
    font-size: 29px; color: var(--ink-blue);
  }
</style>
</head>
<body>
<main class="signage">
  <div class="hero-panel">
    <svg viewBox="0 0 500 152" width="500" height="152" aria-hidden="true">
      <path d="M14 2 H484 Q498 2 498 16 V96 Q498 104 492 111 L455 146 Q450 150 443 150 H14 Q2 150 2 138 V14 Q2 2 14 2 Z"
            fill="var(--panel)" stroke="var(--panel-edge)" stroke-width="2"/>
    </svg>
  </div>

  <div class="mascot" role="img" aria-label="Masked burglar character peeking around the panel edge"></div>

  <h1 class="headline">YOUR <span class="hl">HOME</span><br>AS <span class="hl">SAFE</span> AS<br>YOU WANT?</h1>

  <div class="brand-name">KVS</div>
  <div class="brand-tagline">KESTREL VANTAGE SYSTEMS</div>

  <ul class="services">
    <li class="service alarms">
      <svg viewBox="0 0 32 32" aria-hidden="true"><rect width="32" height="32" rx="6" fill="#ffffff" opacity=".2"/><path d="M16 6 c-5 0 -7 4 -7 8 v5 l-3 4 h20 l-3 -4 v-5 c0 -4 -2 -8 -7 -8z M13 25 a3 3 0 0 0 6 0z" fill="#fff"/></svg>
      <span>ALARMS</span>
    </li>
    <li class="service intercoms">
      <svg viewBox="0 0 32 32" aria-hidden="true"><rect x="5" y="3" width="22" height="26" rx="3" fill="none" stroke="#fff" stroke-width="2"/><rect x="9" y="7" width="14" height="9" fill="#fff" opacity=".8"/><circle cx="12" cy="22" r="2" fill="#fff"/><circle cx="19" cy="22" r="2" fill="#fff"/></svg>
      <span>INTERCOMS</span>
    </li>
    <li class="service cctv">
      <svg viewBox="0 0 32 32" aria-hidden="true"><path d="M4 10 L24 6 L27 14 L7 18 Z" fill="#fff"/><path d="M14 17 L15 22 H6 V26 H3 V17 Z" fill="#fff"/></svg>
      <span>CCTV</span>
    </li>
    <li class="service access">
      <svg viewBox="0 0 32 32" aria-hidden="true"><g fill="#fff"><rect x="3" y="3" width="6" height="6"/><rect x="11" y="3" width="6" height="6"/><rect x="3" y="11" width="6" height="6"/><rect x="11" y="11" width="6" height="6"/><rect x="3" y="19" width="6" height="6"/><path d="M19 14 h4 v8 h4 l2 4 -3 5 h-8 l-3 -6 h4z"/></g></svg>
      <span>ACCESS<br>CONTROL</span>
    </li>
  </ul>

  <div class="phone">
    <svg viewBox="0 0 34 30" aria-hidden="true"><path d="M3 10 Q17 0 31 10 L28 15 L23 13 L22 9 Q17 7 12 9 L11 13 L6 15 Z" fill="var(--ink-blue)"/><path d="M9 15 H25 L29 28 H5 Z" fill="var(--ink-blue)"/><circle cx="17" cy="21" r="4" fill="#fff"/></svg>
    <span>0400 555 018</span>
  </div>

  <div class="website">WWW.KESTRELVANTAGE.COM</div>
</main>
</body>
</html>
```